Brightfold Partners Website

Brightfold Partners Advisory Services is a company which provides specialised advise in carbon markets, climate policy, landscapes, resilience and change. We are based in Australia but the majority of our business is global. Our clients range from governments to large corporates and not for profit organisations.
Our focus is on developing the capabilities of government officials, business decision makers and land managers so they can better navigate the complexity of climate change and sustainability.
We are looking for a website that is consistent with the high end professional services which we provide to serious players.
I have attached two versions of our logo. I have also attached the back of our business card so you can get a sense of what we hand to potential clients.

Target Market(s)

Professional individuals, decision makers, board members etc, government officials.

Industry/Entity Type

Government

Number of Pages Required

4 page

Font styles to use
Serif
Sans Serif

Requirements
Must have
• Please provide
• 1. Home page
• 2. Service page template
• 3. Contact page
• 4. Lead expert profile page

```html
<!DOCTYPE html>
<html lang="en">
<head>
<meta charset="utf-8">
<title>Brightfold Partners</title>
<link rel="stylesheet" href="https://fonts.googleapis.com/css2?family=Lora:wght@400;700&family=Open+Sans:wght@400;600&display=swap">
<style>
:root{
  --ink:#222831;
  --ink-soft:#2b3038;
  --body:#8a8d92;
  --rule:#d9dbde;
  --band:#f8f8f8;
  --white:#ffffff;
  --hero-a:#5d6670;
  --hero-b:#8f98a0;
  --contact-a:#3d4a55;
  --contact-b:#6f7c86;
  --field:rgba(236,238,239,0.92);
}
*{margin:0;padding:0;box-sizing:border-box}
html,body{width:1200px;height:2466px;overflow:hidden;background:var(--white)}
body{position:relative;font-family:"Open Sans",Arial,sans-serif;color:var(--ink)}
.serif{font-family:"Lora",Georgia,serif}

/* hero */
.hero{position:absolute;left:0;top:0;width:1200px;height:612px;overflow:hidden}
.hero-photo{position:absolute;inset:0;background:linear-gradient(120deg,var(--hero-a),var(--hero-b) 50%,#6e7780)}
.hero-shade{position:absolute;inset:0;background:rgba(40,48,56,0.35)}
.social-top{position:absolute;left:170px;top:26px;display:flex;gap:16px}
.social-top span{width:14px;height:14px;border-radius:50%;background:rgba(255,255,255,0.8)}
.nav{position:absolute;top:25px;left:0;width:1200px;font-family:"Lora",Georgia,serif;font-size:15px;color:var(--white);letter-spacing:.5px}
.nav a{position:absolute;color:inherit;text-decoration:none}
.brand-mark{position:absolute;left:526px;top:125px;width:140px;height:140px;border-radius:50%;background:var(--white)}
.brand-rule{position:absolute;left:428px;width:344px;height:1px;background:rgba(255,255,255,0.6)}
.brand-name{position:absolute;left:0;width:1200px;top:300px;text-align:center;font-family:"Lora",Georgia,serif;font-weight:400;color:var(--white);font-size:42px;line-height:48px;letter-spacing:7px}
.hero-contact{position:absolute;top:436px;font-size:12px;color:var(--white);display:flex;align-items:center;gap:8px}
.scroll-down{position:absolute;left:567px;top:522px}

/* welcome */
.welcome{position:absolute;top:612px;left:0;width:1200px;height:418px}
.welcome h1{position:absolute;top:48px;width:1200px;text-align:center;font-family:"Lora",Georgia,serif;font-weight:700;font-size:25px;letter-spacing:.5px}
.tagline{position:absolute;top:80px;left:343px;width:514px;display:flex;align-items:center;gap:14px;font-size:13px;color:#55595e}
.tagline::before,.tagline::after{content:"";flex:1;height:1px;background:var(--rule)}

/* service rows */
.band{position:absolute;left:0;width:1200px;background:var(--band)}
.service-photo{position:absolute;width:424px;height:230px}
.service-text{position:absolute;width:407px}
.service-text h2{font-family:"Lora",Georgia,serif;font-weight:700;font-size:22px;letter-spacing:.5px;border-top:1px solid var(--rule);border-bottom:1px solid var(--rule);padding:9px 0 8px}
.service-text p{margin-top:12px;font-size:10.6px;line-height:14.3px;color:var(--body)}
.read-more{display:inline-block;margin-top:14px;width:113px;height:31px;line-height:31px;text-align:center;background:var(--ink-soft);color:var(--white);font-family:"Lora",Georgia,serif;font-weight:700;font-size:10px;letter-spacing:.5px}

/* contact */
.contact{position:absolute;left:0;top:1979px;width:1200px;height:391px;overflow:hidden}
.contact-photo{position:absolute;inset:0;background:linear-gradient(100deg,var(--contact-a),var(--contact-b) 55%,#4a5661)}
.contact-shade{position:absolute;inset:0;background:rgba(30,38,46,0.3)}
.contact-mark{position:absolute;left:418px;top:40px;width:72px;height:72px;border-radius:50%;background:var(--white)}
.contact h2{position:absolute;left:510px;top:56px;font-family:"Lora",Georgia,serif;font-weight:700;font-size:27px;color:var(--white);letter-spacing:.5px}
.field{position:absolute;background:var(--field);font-family:"Lora",Georgia,serif;font-size:11px;color:#555;padding:12px 0 0 18px;letter-spacing:.5px}
.send{position:absolute;left:290px;top:306px;width:618px;height:41px;background:var(--ink-soft);color:var(--white);font-family:"Lora",Georgia,serif;font-size:12px;text-align:center;line-height:41px;letter-spacing:.5px}

/* footer */
.footer{position:absolute;left:0;top:2370px;width:1200px;height:96px}
.footer-note{position:absolute;left:177px;top:38px;font-family:"Lora",Georgia,serif;font-size:14px;color:#444}
.footer-mark{position:absolute;left:578px;top:28px;width:40px;height:40px;border-radius:50%;background:#b9bcc0}
.social-foot{position:absolute;left:882px;top:34px;display:flex;gap:11px}
.social-foot span{width:28px;height:28px;border-radius:50%}
</style>
</head>
<body>

<header class="hero">
  <div class="hero-photo" role="img" aria-label="Photograph of a business team meeting in a bright office"></div>
  <div class="hero-shade"></div>
  <div class="social-top"><span></span><span></span><span></span><span></span></div>
  <nav class="nav">
    <a style="left:672px">HOME</a>
    <a style="left:752px">SERVICES</a>
    <a style="left:859px">PROFILE</a>
    <a style="left:953px">CONTACT</a>
  </nav>
  <div class="brand-mark"></div>
  <div class="brand-rule" style="top:294px"></div>
  <div class="brand-name">BRIGHTFOLD<br>PARTNERS</div>
  <div class="brand-rule" style="top:417px"></div>
  <div class="hero-contact" style="left:430px">
    <svg width="14" height="14" viewBox="0 0 24 24" fill="none" stroke="#fff" stroke-width="2"><path d="M5 3h4l2 5-3 2a12 12 0 0 0 6 6l2-3 5 2v4a2 2 0 0 1-2 2A18 18 0 0 1 3 5a2 2 0 0 1 2-2z"/></svg>
    0800 (555) 0199
  </div>
  <div class="hero-contact" style="left:600px">
    <svg width="16" height="14" viewBox="0 0 24 20" fill="none" stroke="#fff" stroke-width="2"><rect x="2" y="3" width="20" height="14"/><path d="M2 3l10 8 10-8"/></svg>
    info@brightfoldpartners.com
  </div>
  <svg class="scroll-down" width="58" height="58" viewBox="0 0 58 58" fill="none" stroke="rgba(255,255,255,0.75)" stroke-width="1.5"><circle cx="29" cy="29" r="27"/><path d="M20 25l9 9 9-9"/></svg>
</header>

<section class="welcome">
  <h1>WELCOME TO THE BRIGHTFOLD PARTNERS !</h1>
  <div class="tagline">Brightfold Partners Advisory Services</div>
</section>

<!-- carbon markets -->
<div class="service-photo" style="left:171px;top:762px;background:linear-gradient(135deg,#7fa6c2,#c9d6df 55%,#5f7d99)" role="img" aria-label="Photograph of a confident team of business people"></div>
<article class="service-text" style="left:621px;top:762px">
  <h2>CARBON MARKETS</h2>
  <p>We help governments, corporates and not for profit organisations understand carbon markets and act with confidence. Our advisers combine policy depth with practical field experience, building the capability of officials, decision makers and land managers so they can navigate complexity, design credible programs and deliver lasting results for their communities and the landscapes they care for across the globe. Every engagement is shaped around clear goals, sound evidence and practical steps.</p>
  <span class="read-more">READ MORE</span>
</article>

<!-- climate policy -->
<div class="band" style="top:1028px;height:324px"></div>
<article class="service-text" style="left:173px;top:1075px">
  <h2>CLIMATE POLICY</h2>
  <p>We help governments, corporates and not for profit organisations understand climate policy and act with confidence. Our advisers combine policy depth with practical field experience, building the capability of officials, decision makers and land managers so they can navigate complexity, design credible programs and deliver lasting results for their communities and the landscapes they care for across the globe. Every engagement is shaped around clear goals, sound evidence and practical steps.</p>
  <span class="read-more">READ MORE</span>
</article>
<div class="service-photo" style="left:604px;top:1075px;background:linear-gradient(135deg,#d8cfc6,#a79a90 50%,#5a5250)" role="img" aria-label="Photograph of colleagues reviewing documents together at a desk"></div>

<!-- landscapes -->
<div class="service-photo" style="left:171px;top:1387px;background:linear-gradient(135deg,#e6e8ea,#b9c0c9 50%,#6b7684)" role="img" aria-label="Photograph of three professionals in a boardroom discussion"></div>
<article class="service-text" style="left:621px;top:1387px">
  <h2>LANDSCAPES</h2>
  <p>We help governments, corporates and not for profit organisations understand landscape change and act with confidence. Our advisers combine policy depth with practical field experience, building the capability of officials, decision makers and land managers so they can navigate complexity, design credible programs and deliver lasting results for their communities and the landscapes they care for across the globe. Every engagement is shaped around clear goals, sound evidence and practical steps.</p>
  <span class="read-more">READ MORE</span>
</article>

<!-- resilience -->
<div class="band" style="top:1654px;height:323px"></div>
<article class="service-text" style="left:173px;top:1702px">
  <h2>RESILIENCE</h2>
  <p>We help governments, corporates and not for profit organisations understand resilience planning and act with confidence. Our advisers combine policy depth with practical field experience, building the capability of officials, decision makers and land managers so they can navigate complexity, design credible programs and deliver lasting results for their communities and the landscapes they care for across the globe. Every engagement is shaped around clear goals, sound evidence and practical steps.</p>
  <span class="read-more">READ MORE</span>
</article>
<div class="service-photo" style="left:604px;top:1702px;background:linear-gradient(135deg,#9fb8cf,#e3e9ee 55%,#c4ccd3)" role="img" aria-label="Photograph of hands signing a document with a pen"></div>

<section class="contact">
  <div class="contact-photo" role="img" aria-label="Photograph of a meeting table with glasses and papers"></div>
  <div class="contact-shade"></div>
  <div class="contact-mark"></div>
  <h2>CONTACT US NOW !</h2>
  <div class="field" style="left:290px;top:140px;width:306px;height:42px">NAME</div>
  <div class="field" style="left:602px;top:140px;width:306px;height:42px">EMAIL</div>
  <div class="field" style="left:290px;top:191px;width:618px;height:111px">MESSAGE</div>
  <div class="send">SEND</div>
</section>

<footer class="footer">
  <div class="footer-note">Brightfold Partners © 2014 Privacy Policy</div>
  <div class="footer-mark"></div>
  <div class="social-foot">
    <span style="background:#4a4fa0"></span>
    <span style="background:#3fa7dd"></span>
    <span style="background:#e2493b"></span>
    <span style="background:#d42a2a"></span>
  </div>
</footer>

</body>
</html>
```